Web site for Velto Grounded Consulting Pty. Ltd.

Create a modern website that is contemporary and appropriate for a business that is a provider of Consulting services to businesses. The LOGO is provided below. The consulting services offered are Supply Chain Management, 4th Party Logistics, Sales Coaching and training, HR services and training (i.e. Sexual Harassment and Bullying policies etc. ) , OH&S Training, Management mentoring, Business strategy and tactical consultations and Union related contract negotiations with award inclusion.

Target Market(s)

Importers, Exporters, Manufacturers, Freight Forwarders, Companies with large sales teams, warehouse operators

Industry/Entity Type

Business

Coding

Coded - Design and coding required

Number of Pages Required

5+ page

Font styles to use
Serif
Sans Serif

Colors

Designer to choose colors to be used in the design.

Requirements
Must have
• Sky Line Photographs of Sydney and Manhattan, Pictures of people and teams in professional settings with tasteful clothing. Elements of both femininity and masculinity. People photos need to be diverse and include multiple nationalities, races and genders. Must have blog spot and also include the background info of the owners. Linked In pages includes.
Nice to have
• Would like to try both color and / or black and white.
Should not have
• Open

```html
<!DOCTYPE html>
<html lang="en">
<head>
<meta charset="utf-8">
<title>Velto Grounded Consulting</title>
<link rel="stylesheet" href="https://fonts.googleapis.com/css2?family=Exo+2:wght@300;400&family=Arimo:wght@400;700&display=swap">
<style>
:root{
  --page-bg:#3b3b3b;
  --panel:#ffffff;
  --brand:#00916e;
  --ink:#1b1b1b;
  --muted:#6a6a6a;
  --rule:#cfcfcf;
  --nav-active:#3d8fc8;
  --footer-text:#b9b9b9;
  --footer-rule:#4d4d4d;
  --hero-top:#1d3b5e;
  --hero-mid:#5a7fa6;
  --hero-low:#dfe8f1;
}
*{box-sizing:border-box;margin:0;padding:0}
html,body{width:960px;height:1200px;overflow:hidden}
body{background:var(--page-bg);font-family:"Arimo",Arial,sans-serif;position:relative}
.abs{position:absolute}
.panel{left:77px;top:0;width:800px;height:958px;background:var(--panel)}
.hero{left:77px;top:0;width:800px;height:424px;
  background:linear-gradient(180deg,var(--hero-top) 0%,var(--hero-mid) 45%,var(--hero-low) 100%)}
.logo{left:110px;top:90px;color:#fff;font-family:"Exo 2",sans-serif;font-weight:300}
.logo-name{font-size:54px;line-height:54px;letter-spacing:1px}
.logo-sub{font-size:15px;letter-spacing:1px;margin-top:4px}
.nav{left:610px;top:31px;display:flex;height:24px;font-family:"Exo 2",sans-serif;font-size:10.5px;color:#fff}
.nav a{color:#fff;text-decoration:none;padding:0 9px;line-height:24px;white-space:nowrap}
.nav a.active{background:var(--nav-active);padding:0 12px}
.tagline{left:101px;top:411px;width:752px;height:38px;background:var(--brand);color:#fff;white-space:nowrap;overflow:hidden;
  font-family:"Exo 2",sans-serif;font-weight:300;font-size:18px;line-height:38px;padding-left:9px;letter-spacing:-.3px}
.h-section{font-family:"Exo 2",sans-serif;font-weight:300;color:var(--ink)}
.h-section span{color:var(--brand)}
.welcome{left:100px;top:468px;font-size:19px}
.welcome-rule{left:101px;top:496px;width:752px;height:1px;background:var(--rule)}
.dots{left:795px;top:469px;display:flex;gap:3px}
.dots i{width:9px;height:9px;border-radius:50%;background:#b4b4b4;border:1px solid #999}
.dots i.on{background:#444}
.intro{left:103px;top:505px;width:758px;font-size:9.6px;line-height:16px;color:var(--muted)}
.btn{display:inline-flex;align-items:center;gap:8px;height:20px;padding:0 7px 0 9px;font-size:8px;color:#333;white-space:nowrap;
  background:linear-gradient(#fff,#ececec);border:1px solid #cfcfcf;border-radius:2px;text-decoration:none}
.btn svg{width:6px;height:9px;flex:none}
.btn-intro{left:786px;top:574px}
.services-title{left:0;width:960px;top:619px;text-align:center;font-size:19px}
.services-rule{left:101px;top:649px;width:752px;height:1px;background:var(--rule)}
.service{width:178px}
.service h3{font-family:"Exo 2",sans-serif;font-weight:300;font-size:15px;color:var(--ink);
  line-height:14px;padding-bottom:6px;border-bottom:1px solid var(--rule);height:20px;white-space:nowrap}
.service h3 span{color:var(--brand)}
.service .photo{margin-top:18px;height:128px;box-shadow:0 4px 4px -3px rgba(0,0,0,.25)}
.service p{margin-top:19px;font-size:8.3px;line-height:16px;color:var(--muted)}
.service .btn{margin-top:12px;margin-left:-3px}
.footer-h{font-family:"Exo 2",sans-serif;font-weight:300;font-size:15px;color:#d6d6d6;top:983px}
.flist{list-style:none;width:128px;top:1010px}
.flist li{height:24px;line-height:24px;font-size:8px;color:var(--footer-text);border-bottom:1px solid var(--footer-rule);
  padding-left:11px;position:relative;white-space:nowrap}
.flist li:last-child{border-bottom:none}
.flist li::before{content:"";position:absolute;left:1px;top:9px;border-left:4px solid #777;border-top:3px solid transparent;border-bottom:3px solid transparent}
.client{left:292px;top:1014px;width:139px;height:110px;background:#fff;display:flex;align-items:center;justify-content:center;
  font-family:"Exo 2",sans-serif;font-weight:400;font-size:22px;color:var(--brand)}
.client-arrows{left:407px;top:1139px;display:flex;gap:8px}
.contact{left:673px;top:1010px;font-size:8px;line-height:16px;color:var(--footer-text);font-style:normal}
.foot-rule{left:77px;top:1164px;width:800px;height:1px;background:var(--footer-rule)}
.copy{left:77px;top:1172px;font-size:9px;color:var(--footer-text)}
.copy b{color:#dcdcdc}
</style>
</head>
<body>
<div class="abs panel"></div>

<header>
  <div class="abs hero" role="img" aria-label="Photo of a goldfish leaping from a small fishbowl into a larger one"></div>
  <div class="abs logo">
    <div class="logo-name">Velto</div>
    <div class="logo-sub">Grounded Consulting</div>
  </div>
  <nav class="abs nav">
    <a class="active" href="#">Home</a><a href="#">About Us</a><a href="#">Services</a><a href="#">Blog</a><a href="#">Contact</a>
  </nav>
  <div class="abs tagline">Velto Grounded Consulting Pty. Ltd provider of Consulting services to businesses.</div>
</header>

<main>
  <h1 class="abs h-section welcome">Welcome <span>to Velto Grounded Consulting</span></h1>
  <div class="abs dots"><i></i><i></i><i></i><i></i><i class="on"></i></div>
  <div class="abs welcome-rule"></div>
  <p class="abs intro">Our consulting services focus on our clients' most critical issues and opportunities. Praesent malesuada mauris a odio adipiscing mollis. Invarius tincidunt elit vitae eleifend. Etiam fermentum suscipit est vel aliquet. Quisque malesuada luctus dignissim bibendum a lobortis mauris placerat.Donec quam felis, ultricies nec, pellentesque eu, pretium quis, sem. Nulla consequat massa quis enim. Lorem ipsum dolor sit amet, consectetur adipiscing elit. Morbi id tristique sem. Nuncnec ipsum sed nisi dictum mollis. Praesent malesuada mauris a odio adipiscing mollis.</p>
  <a class="abs btn btn-intro" href="#">read more <svg viewBox="0 0 6 9"><path d="M1 1l4 3.5L1 8z" fill="none" stroke="#888"/></svg></a>

  <h2 class="abs h-section services-title">Our <span>Services</span></h2>
  <div class="abs services-rule"></div>

  <section class="abs service" style="left:101px;top:664px">
    <h3>Supply <span>Chain Management</span></h3>
    <div class="photo" role="img" aria-label="Photo of hands joining puzzle pieces" style="background:linear-gradient(135deg,#1c2330,#6b6f76 50%,#2a2e36)"></div>
    <p>Are your competitors talking about you in their boardrooms? Does your strategy guide how you allocate resources.</p>
    <a class="btn" href="#">read more <svg viewBox="0 0 6 9"><path d="M1 1l4 3.5L1 8z" fill="none" stroke="#888"/></svg></a>
  </section>
  <section class="abs service" style="left:292px;top:664px">
    <h3>Sales <span>Coaching &nbsp;&amp; training</span></h3>
    <div class="photo" role="img" aria-label="Photo of a businesswoman with a laptop showing charts" style="background:linear-gradient(135deg,#f1f1f1,#d9d4cc 50%,#b9c9dc)"></div>
    <p>Are your competitors talking about you in their boardrooms? Does your strategy guide how you allocate resources.</p>
    <a class="btn" href="#">read more <svg viewBox="0 0 6 9"><path d="M1 1l4 3.5L1 8z" fill="none" stroke="#888"/></svg></a>
  </section>
  <section class="abs service" style="left:483px;top:664px">
    <h3>HR <span>Services &amp; Training</span></h3>
    <div class="photo" role="img" aria-label="Photo of a team with headsets in a call centre" style="background:linear-gradient(135deg,#8f96a0,#e6e8ea 55%,#c9ccd0)"></div>
    <p>Are your competitors talking about you in their boardrooms? Does your strategy guide how you allocate resources.</p>
    <a class="btn" href="#">read more <svg viewBox="0 0 6 9"><path d="M1 1l4 3.5L1 8z" fill="none" stroke="#888"/></svg></a>
  </section>
  <section class="abs service" style="left:674px;top:664px">
    <h3>Management <span>Mentoring</span></h3>
    <div class="photo" role="img" aria-label="Photo of two colleagues reviewing documents at a desk" style="background:linear-gradient(135deg,#cfd6de,#8a8f98 50%,#e4e1dc)"></div>
    <p>Are your competitors talking about you in their boardrooms? Does your strategy guide how you allocate resources.</p>
    <a class="btn" href="#">read more <svg viewBox="0 0 6 9"><path d="M1 1l4 3.5L1 8z" fill="none" stroke="#888"/></svg></a>
  </section>
</main>

<footer>
  <h4 class="abs footer-h" style="left:99px">Our Services</h4>
  <ul class="abs flist" style="left:100px">
    <li>Supply Chain Management</li><li>4th Party Logistics</li><li>Sales Coaching and training</li>
    <li>HR services and training</li><li>OH&amp;S Training</li><li>Business strategy</li>
  </ul>

  <h4 class="abs footer-h" style="left:290px">Our Client's</h4>
  <div class="abs client">Corvane</div>
  <div class="abs client-arrows">
    <svg width="8" height="14" viewBox="0 0 8 14"><path d="M7 1L1 7l6 6" fill="none" stroke="#bbb" stroke-width="1.3"/></svg>
    <svg width="8" height="14" viewBox="0 0 8 14"><path d="M1 1l6 6-6 6" fill="none" stroke="#bbb" stroke-width="1.3"/></svg>
  </div>

  <h4 class="abs footer-h" style="left:482px">Site Map</h4>
  <ul class="abs flist" style="left:482px">
    <li>Home Page</li><li>About Us</li><li>Services</li><li>Blog Page</li><li>Contact Us</li>
  </ul>

  <h4 class="abs footer-h" style="left:673px">Contact Us</h4>
  <address class="abs contact">
    Velto Grounded Consulting Pty. Ltd.<br>PO Box No 12345<br>Some guy`s name St, Town<br>New Something 1234, Country<br><br>
    Telephone/Fax: 1234 5678<br><br>
    General: email@veltogroundedconsulting.com<br>Support: email@veltogroundedconsulting.com
  </address>

  <div class="abs foot-rule"></div>
  <p class="abs copy">© 2017 Copyright <b>Velto Grounded Consulting Pty. Ltd.</b>. All Rights Reserved</p>
</footer>
</body>
</html>
```